Marlo Vista Table & Chair Rentals

We need a business card for a table and chair rental company. We rent tables and chairs for weddings, funerals, business events and parties. We want something that looks clean and elegant while not being too busy. We would like colors in the green and blue hues and avoiding anything orange. We want to make sure the font is large enough to be seen easily.

Target Market(s)

Wedding & Event Rentals

Industry/Entity Type

Events

Contact Information for Business Card

Marlo Vista, sales@marlovistarentals.example, marlovistarentals.example, 360-555-0182

Requirements
Must have
• Easy to read font
Should not have
• Orange anywhere in the design

```html
<!DOCTYPE html>
<html lang="en">
<head>
<meta charset="utf-8">
<title>Marlo Vista Table &amp; Chair Rentals — Business Card</title>
<link rel="stylesheet" href="https://fonts.googleapis.com/css2?family=Quicksand:wght@400;500&display=swap">
<style>
  :root {
    --backdrop: #dcdcdc;
    --card-green: #86b61f;
    --card-blue: #33b4e4;
    --disc: #f4f4f2;
    --name-green: #86b61f;
    --contact-white: #ffffff;
    --card-shadow: rgba(0, 0, 0, 0.12);
  }
  * { box-sizing: border-box; margin: 0; padding: 0; }
  html, body {
    width: 1200px;
    height: 900px;
    overflow: hidden;
  }
  body {
    background: var(--backdrop);
    font-family: "Quicksand", sans-serif;
    position: relative;
  }
  .card {
    position: absolute;
    width: 500px;
    height: 286px;
    box-shadow: 0 2px 6px var(--card-shadow);
  }
  .card--front {
    left: 160px;
    top: 150px;
    background: var(--card-green);
  }
  .card--back {
    left: 540px;
    top: 464px;
    background: var(--card-blue);
  }
  .disc {
    position: absolute;
    border-radius: 50%;
    background: var(--disc);
    display: flex;
    align-items: center;
    justify-content: center;
  }
  .card--front .disc {
    width: 180px;
    height: 180px;
    left: 205px;
    top: 53px;
  }
  .card--back .disc {
    width: 118px;
    height: 118px;
    left: 32px;
    top: 84px;
  }
  .brand-name {
    color: var(--name-green);
    font-weight: 500;
    letter-spacing: 0.02em;
    white-space: nowrap;
  }
  .card--front .brand-name { font-size: 25px; }
  .card--back .brand-name { font-size: 16px; }
  .contact-list {
    position: absolute;
    left: 196px;
    top: 104px;
    list-style: none;
    color: var(--contact-white);
    font-weight: 400;
    font-size: 16px;
    line-height: 1;
  }
  .contact-item {
    display: flex;
    align-items: center;
    gap: 9px;
    margin-bottom: 12px;
    white-space: nowrap;
  }
  .contact-icon {
    width: 16px;
    height: 16px;
    flex: none;
  }
</style>
</head>
<body>
  <section class="card card--front" aria-label="Business card front">
    <div class="disc">
      <span class="brand-name">marlo vista</span>
    </div>
  </section>

  <section class="card card--back" aria-label="Business card back">
    <div class="disc">
      <span class="brand-name">marlo vista</span>
    </div>
    <ul class="contact-list">
      <li class="contact-item">
        <svg class="contact-icon" viewBox="0 0 16 16" aria-hidden="true">
          <circle cx="8" cy="8" r="8" fill="#fff"/>
          <rect x="4" y="5.2" width="8" height="5.6" rx="0.6" fill="none" stroke="#33b4e4" stroke-width="1.1"/>
          <path d="M4.3 5.6 L8 8.4 L11.7 5.6" fill="none" stroke="#33b4e4" stroke-width="1.1"/>
        </svg>
        <span>sales@marlovistarentals.example</span>
      </li>
      <li class="contact-item">
        <svg class="contact-icon" viewBox="0 0 16 16" aria-hidden="true">
          <circle cx="8" cy="8" r="8" fill="#fff"/>
          <g fill="none" stroke="#33b4e4" stroke-width="1">
            <circle cx="8" cy="8" r="4.6"/>
            <ellipse cx="8" cy="8" rx="2" ry="4.6"/>
            <line x1="3.4" y1="8" x2="12.6" y2="8"/>
          </g>
        </svg>
        <span>marlovistarentals.example</span>
      </li>
      <li class="contact-item">
        <svg class="contact-icon" viewBox="0 0 16 16" aria-hidden="true">
          <circle cx="8" cy="8" r="8" fill="#fff"/>
          <path d="M5.4 4.2 L6.8 4 L7.4 6.1 L6.5 6.9 C7 8 7.9 8.9 9 9.5 L9.8 8.6 L11.9 9.2 L11.7 10.6 C11.5 11.3 10.8 11.7 10.1 11.6 C7.3 11 5 8.7 4.4 5.9 C4.3 5.1 4.7 4.4 5.4 4.2 Z" fill="#33b4e4"/>
        </svg>
        <span>360-555-0182</span>
      </li>
    </ul>
  </section>
</body>
</html>
```